One Page Sales Flyer for Wireless Survey- Computer Hardware

I want a designer to create a one page 4 color sales slick to be given to our sales team to sell to the end customers. I would like a visual picture of a heat map so zavvix "heat map wireless" to get an idea of how that image should look.

```html
<!DOCTYPE html>
<html lang="en">
<head>
<meta charset="utf-8">
<title>Quorvelt – Wireless Site Survey Sales Sheet</title>
<link rel="stylesheet" href="https://fonts.googleapis.com/css2?family=Teko:wght@400;500&family=Montserrat:wght@400;500;600&family=Hind:ital,wght@0,400;0,600;0,700;1,400;1,600&display=swap">
<style>
  :root {
    --stage: #3ea7e0;
    --brand-blue: #2b9fdc;
    --ink: #2f2f31;
    --panel-dark: #1d1d1f;
    --logo-bar: #2c2c2e;
    --body-text: #cfcfcf;
    --white: #ffffff;
  }
  * { box-sizing: border-box; margin: 0; padding: 0; }
  html, body { width: 1200px; height: 1000px; overflow: hidden; }
  body { background: var(--stage); font-family: "Hind", sans-serif; position: relative; }

  .sheet {
    position: absolute; left: 312px; top: 68px; width: 598px; height: 844px;
    background: var(--panel-dark); overflow: hidden;
  }

  /* Hero */
  .hero {
    position: absolute; left: 0; top: 0; width: 598px; height: 390px;
    background: linear-gradient(135deg, #f6f6f6 0%, #e4e4e4 55%, #d9d9d9 100%);
  }
  .hero::after {
    content: ""; position: absolute; left: 0; bottom: 0; width: 100%; height: 6px; background: #3a3a3c;
  }
  .brand-bar {
    position: absolute; left: 0; top: 17px; width: 310px; height: 80px;
    background: var(--logo-bar); border-right: 12px solid var(--brand-blue);
    display: flex; align-items: center; padding-left: 38px; gap: 14px;
  }
  .brand-square { width: 48px; height: 48px; background: var(--brand-blue); border-radius: 6px; }
  .brand-name {
    font-family: "Montserrat", sans-serif; font-weight: 400; font-size: 28px;
    color: var(--white); letter-spacing: 1px;
  }
  .headline {
    position: absolute; left: 35px; top: 126px;
    font-family: "Teko", sans-serif; font-weight: 500; font-size: 40px; line-height: 40px;
    color: var(--ink); text-transform: uppercase;
  }
  .headline .accent { color: var(--brand-blue); }
  .heatmap-art {
    position: absolute; left: 368px; top: 8px; width: 230px; height: 378px;
    background: radial-gradient(ellipse at 55% 25%, #8fd0ee 0%, #a9dcf2 30%, rgba(190,226,243,0.6) 60%, rgba(230,230,230,0) 85%),
                radial-gradient(ellipse at 60% 78%, #7cc6ea 0%, rgba(160,214,240,0.7) 45%, rgba(230,230,230,0) 80%);
  }

  /* Content */
  .block { position: absolute; color: var(--body-text); }
  .block h2 {
    font-family: "Montserrat", sans-serif; font-weight: 500; font-size: 13px; line-height: 17px;
    color: var(--brand-blue); margin-bottom: 14px; max-width: 220px;
  }
  .block h2 strong { color: var(--white); font-weight: 600; font-size: 16px; }
  .block p { font-size: 9px; line-height: 12.4px; text-align: justify; }
  .block p em { font-style: italic; }
  .what { left: 34px; top: 420px; width: 266px; }
  .why-need { left: 333px; top: 420px; width: 232px; }
  .why-you { left: 34px; top: 564px; width: 268px; }
  .targets { left: 331px; top: 564px; width: 200px; }

  .reason-list { list-style: none; }
  .reason-list li { display: flex; gap: 14px; font-size: 9px; line-height: 12.4px; }
  .reason-list li > span:last-child { width: 237px; text-align: justify; }
  .reason-list li:nth-child(1) { height: 37px; }
  .reason-list li:nth-child(2) { height: 73px; }
  .reason-list li:nth-child(3) { height: 49px; }
  .reason-icon {
    flex: none; width: 17px; height: 17px; border: 2px solid var(--brand-blue); border-radius: 3px;
    position: relative; margin-top: 1px;
  }
  .reason-icon::after {
    content: ""; position: absolute; left: 3px; top: 3px; width: 7px; height: 7px; background: var(--brand-blue);
  }
  .reason-list strong { color: var(--white); font-weight: 700; }

  .target-list { list-style: none; margin-top: 0; }
  .target-list li {
    font-size: 10.5px; line-height: 18.7px; color: var(--body-text); padding-left: 18px; position: relative;
  }
  .target-list li::before {
    content: ""; position: absolute; left: 3px; top: 8px; width: 5px; height: 5px; border-radius: 50%; background: var(--brand-blue);
  }
  .source-note {
    position: absolute; left: 318px; top: 797px; font-size: 8px; color: var(--body-text);
  }

  .contact-band {
    position: absolute; left: 0; bottom: 0; width: 598px; height: 34px; background: var(--brand-blue);
    display: flex; align-items: center; justify-content: center;
    font-family: "Montserrat", sans-serif; font-weight: 600; font-size: 12.5px; letter-spacing: 1.4px; color: var(--white);
  }
</style>
</head>
<body>
  <main class="sheet">
    <header class="hero">
      <div class="brand-bar">
        <span class="brand-square"></span>
        <span class="brand-name">QUORVELT</span>
      </div>
      <h1 class="headline">
        <span class="accent">Increase</span><br>
        Hardware<br>
        <span class="accent">and</span> Services<br>
        Spend with<br>
        <span class="accent">Wireless</span><br>
        <span class="accent">Site</span> Surveys
      </h1>
      <div class="heatmap-art" role="img" aria-label="Floor plan with wireless signal heat map in light blue tones"></div>
    </header>

    <section class="block what">
      <h2><strong>What</strong> is a wireless site survey or heat map?</h2>
      <p>A wireless site survey is a <strong><em>compilation of reports showing a visual representation of health of your wireless network</em></strong>. This does not only show how strong or weak a wireless signal is in any location it also helps aid in channel and placement to ensure maximum stable data rates are archived even where the single appears strong.</p>
    </section>

    <section class="block why-need">
      <h2><strong>Why</strong> do customers need a site survey?</h2>
      <p>Any variety of factors can contribute to an unhealthy wireless network (<em>electrical, motors, materials used in construction, distance, neighboring wireless networks, etc.</em>) and traditional methods that use only blueprints and a computer program to show signal strength have shown to be ineffective.</p>
    </section>

    <section class="block why-you">
      <h2><strong>Why</strong> should they use you?</h2>
      <ul class="reason-list">
        <li><span class="reason-icon"></span><span><strong>42%</strong> of businesses report some issues with wireless connectivity and acknowledge its effect on the bottomline*</span></li>
        <li><span class="reason-icon"></span><span>Most of these problems are solved through either fine tuning the current equipment (<em>managed services</em>) or purchasing new equipment (<em>incremental sales</em>) of which you can provide both.</span></li>
        <li><span class="reason-icon"></span><span>Being a one-stop shop for all your customer's IT needs prevents them from needing additional vendors.</span></li>
        <li><span class="reason-icon"></span><span>The increase of <strong>IoT</strong> (<em>Internet of things</em>) and <strong>BYOD</strong> (<em>Bring Your Own Device</em>).</span></li>
      </ul>
    </section>

    <section class="block targets">
      <h2><strong>Target</strong> Customers</h2>
      <ul class="target-list">
        <li>Distributors</li>
        <li>Warehouses</li>
        <li>Sled</li>
        <li>K012</li>
        <li>Medical/Hospitals</li>
        <li>Enterprise F1000</li>
        <li>Sports Venues</li>
        <li>Stadiums</li>
        <li>Hotels</li>
        <li>Retail Stores</li>
      </ul>
    </section>

    <p class="source-note">*Lumquistwire.com. "Connectivity in the Modern Enterprise". June 2017</p>

    <footer class="contact-band">949-555-0173 | INFO@YOURQUORVELT.COM | WWW.YOURQUORVELT.COM</footer>
  </main>
</body>
</html>
```